BLQ Business Card

We need a business card that reflect our business, we have put anther business card as an example of what we like but please feel free to do your own thing.

Here are the items to be placed on card

Wade Pelham
Amber Harbor Supply
Mobile: 917-555-4820
Office: 516-555-7164
Fax: 866-555-3291
Email: info@amberharborsupply-example.com
Website: amberharborsupply-example.com

I have added raw files to upload

Wade Pelham
Amber Harbor Supply
Mobile: 917-555-4820
Office: 516-555-7164
Fax: 866-555-3291 

Target Market(s)

Natural product manufactures, and retailers and distributors

Industry/Entity Type

Business

Requirements
Must have
• 1. Logo
2. The colors of the company

```html
<!DOCTYPE html>
<html lang="en">
<head>
<meta charset="utf-8">
<title>BLQ Business Card</title>
<link href="https://fonts.googleapis.com/css2?family=Questrial&family=Roboto+Condensed:wght@700&family=Libre+Baskerville:wght@700&display=swap" rel="stylesheet">
<style>
  :root {
    --green: #6ab103;
    --black: #000000;
    --white: #ffffff;
    --page: #ffffff;
    --edge: #d9d9d9;
  }
  * { box-sizing: border-box; margin: 0; padding: 0; }
  html, body { width: 1200px; height: 1000px; overflow: hidden; background: var(--page); }
  .canvas { position: relative; width: 1200px; height: 1000px; }

  .card {
    position: absolute; top: 298px; width: 507px; height: 309px;
    overflow: hidden; background: var(--white);
    box-shadow: 0 0 0 1px var(--edge);
    font-family: "Questrial", sans-serif;
    white-space: nowrap;
  }
  .card--front { left: 78px; }
  .card--back { left: 617px; }

  /* front */
  .front-shapes { position: absolute; inset: 0; }
  .brand-mark {
    position: absolute; left: 40px; top: 150px; width: 180px;
    text-align: center; color: var(--green);
    font-family: "Roboto Condensed", sans-serif; font-weight: 700;
    font-size: 64px; letter-spacing: 4px; line-height: 1;
  }
  .person { position: absolute; left: 222px; top: 68px; width: 284px; text-align: center; }
  .person__name {
    color: var(--white); font-family: "Libre Baskerville", serif; font-weight: 700;
    font-size: 17px; letter-spacing: 0.5px; text-transform: uppercase;
  }
  .person__role { color: var(--green); font-size: 16px; margin-top: 4px; }

  .contact-list { position: absolute; left: 240px; top: 165px; list-style: none; }
  .contact-list li {
    display: flex; align-items: center; height: 22px;
    color: var(--white); font-size: 14px; white-space: nowrap;
  }
  .contact-list li.contact-list__long { font-size: 11.5px; letter-spacing: -0.1px; }
  .contact-list svg { width: 14px; height: 14px; margin-right: 12px; flex: none; }
  .contact-list .sep { width: 2px; height: 12px; background: var(--black); margin-right: 9px; flex: none; }
  .address {
    position: absolute; left: 240px; top: 280px;
    color: var(--white); font-size: 11px; letter-spacing: 0.2px; text-transform: uppercase;
    white-space: nowrap;
  }

  /* back */
  .tagline-band {
    position: absolute; left: 0; top: 0; width: 100%; height: 69px; background: var(--black);
    display: flex; align-items: center; justify-content: center;
  }
  .tagline {
    color: var(--green); font-family: "Roboto Condensed", sans-serif; font-weight: 700; font-size: 26px;
  }
  .company-name {
    position: absolute; left: 0; top: 112px; width: 100%; text-align: center;
    color: var(--green); font-family: "Roboto Condensed", sans-serif; font-weight: 700;
    font-size: 46px; line-height: 1;
  }
  .website { position: absolute; left: 0; top: 217px; width: 100%; text-align: center; font-size: 13px; color: var(--black); }
  .category-band {
    position: absolute; left: 0; top: 240px; width: 100%; height: 69px; background: var(--green);
    padding-top: 11px;
  }
  .category-row { display: flex; justify-content: center; height: 24px; align-items: center; }
  .category-row span { color: var(--white); font-size: 13px; padding: 0 8px; border-left: 2px solid var(--white); line-height: 18px; }
  .category-row span:first-child { border-left: none; }
</style>
</head>
<body>
<div class="canvas">

  <section class="card card--front" aria-label="Front of card">
    <svg class="front-shapes" viewBox="0 0 507 309" width="507" height="309" aria-hidden="true">
      <rect x="0" y="0" width="507" height="309" fill="var(--black)"/>
      <polygon points="0,130 132,66 222,149 222,309 0,309" fill="var(--white)"/>
      <polyline points="0,124 132,72 222,152" fill="none" stroke="var(--green)" stroke-width="10"/>
      <rect x="222" y="149" width="285" height="160" fill="var(--green)"/>
    </svg>

    <div class="brand-mark">BLQ</div>

    <div class="person">
      <div class="person__name">Wade Pelham</div>
      <div class="person__role">Founder</div>
    </div>

    <ul class="contact-list">
      <li>
        <svg viewBox="0 0 14 14"><rect x="3" y="0" width="8" height="14" rx="1.5" fill="var(--black)"/><rect x="4.5" y="2" width="5" height="8" fill="var(--green)"/></svg>
        <span class="sep"></span>917-555-4820
      </li>
      <li>
        <svg viewBox="0 0 14 14"><path d="M1 5 Q7 0 13 5 L11 7 L9 5 L5 5 L3 7 Z" fill="var(--black)"/><rect x="3" y="7" width="8" height="6" rx="1" fill="var(--black)"/></svg>
        <span class="sep"></span>516-555-7164
      </li>
      <li>
        <svg viewBox="0 0 14 14"><rect x="3" y="1" width="8" height="4" fill="var(--black)"/><rect x="0" y="5" width="14" height="6" rx="1" fill="var(--black)"/><rect x="3" y="9" width="8" height="4" fill="var(--black)"/></svg>
        <span class="sep"></span>866-555-3291
      </li>
      <li class="contact-list__long">
        <svg viewBox="0 0 14 14"><rect x="0" y="3" width="14" height="9" fill="var(--black)"/><polyline points="0,3 7,8 14,3" fill="none" stroke="var(--green)" stroke-width="1.2"/></svg>
        <span class="sep"></span>info@amberharborsupply-example.com
      </li>
      <li class="contact-list__long">
        <svg viewBox="0 0 14 14"><circle cx="7" cy="7" r="6.5" fill="var(--black)"/><path d="M4 4 Q7 5 6 8 Q9 9 9 12" fill="none" stroke="var(--green)" stroke-width="1.3"/></svg>
        <span class="sep"></span>www.amberharborsupply-example.com
      </li>
    </ul>

    <div class="address">210 Larkspur Lane, Freeport, NY 11520</div>
  </section>

  <section class="card card--back" aria-label="Back of card">
    <div class="tagline-band"><p class="tagline">Buy or Sell Your Natural Products Direct</p></div>
    <div class="company-name">Amber Harbor Supply</div>
    <div class="website">www.amberharborsupply-example.com</div>
    <div class="category-band">
      <div class="category-row">
        <span>Apparel/Accessories</span><span>Bath &amp; Body</span><span>Beverages</span><span>Books</span><span>Bulk</span><span>Food Service</span>
      </div>
      <div class="category-row">
        <span>Fresh Food</span><span>Frozen</span><span>Grocery</span><span>Herbs &amp; Supplements</span><span>Household</span><span>Snacks</span>
      </div>
    </div>
  </section>

</div>
</body>
</html>
```